Creative & Professional Business Card for hair salon

We are looking to update our business cards. Our salon is creative, modern, progressive and professional and looking for a design that will reflect this.

```html
<!DOCTYPE html>
<html lang="en">
<head>
<meta charset="utf-8">
<title>Mist &amp; Mane — Business Card</title>
<link rel="stylesheet" href="https://fonts.googleapis.com/css2?family=Montserrat:wght@400;700&family=Raleway:wght@300&display=swap">
<style>
  :root {
    --backdrop: #e9edef;
    --teal-deep: #6d97a6;
    --teal-light: #9fbfc7;
    --navy: #4c6f88;
    --ring-light: #8fb2c9;
    --paper: #ffffff;
    --ink: #466a83;
    --paper-ink: #ffffff;
  }
  * { margin: 0; padding: 0; box-sizing: border-box; }
  html, body { width: 1200px; height: 863px; overflow: hidden; }
  body {
    background: var(--backdrop);
    display: flex;
    align-items: center;
    justify-content: center;
    gap: 64px;
    font-family: "Montserrat", Arial, sans-serif;
  }
  .card {
    position: relative;
    width: 340px;
    height: 580px;
    border-radius: 6px;
    overflow: hidden;
    box-shadow: 0 10px 30px rgba(40, 60, 80, 0.18);
  }

  /* Front */
  .card--front {
    background: linear-gradient(160deg, var(--teal-light) 0%, var(--teal-deep) 55%, var(--teal-light) 100%);
  }
  .card--front svg { position: absolute; inset: 0; }
  .brand-lockup {
    position: absolute;
    left: 50%;
    top: 50%;
    transform: translate(-40%, -50%) rotate(90deg);
    display: flex;
    align-items: center;
    gap: 14px;
    white-space: nowrap;
  }
  .brand-name {
    font-family: "Raleway", Arial, sans-serif;
    font-weight: 300;
    font-size: 42px;
    color: var(--ink);
    letter-spacing: 0.5px;
  }
  .brand-dot {
    width: 18px; height: 18px;
    border-radius: 50%;
    background: var(--teal-deep);
  }

  /* Back */
  .card--back { background: var(--paper); }
  .back-mark {
    position: absolute;
    top: 40px; left: 0; right: 0;
    display: flex;
    justify-content: center;
    align-items: center;
    gap: 12px;
  }
  .back-mark .brand-name { font-size: 36px; color: var(--teal-deep); }
  .back-mark .brand-dot { background: var(--teal-deep); }
  .appointment {
    position: absolute;
    top: 168px; left: 34px; right: 34px;
  }
  .appointment__label {
    font-weight: 700;
    font-size: 14px;
    letter-spacing: 0.6px;
    color: var(--ink);
    text-transform: uppercase;
  }
  .appointment__line {
    height: 2px;
    background: var(--ink);
    margin-top: 30px;
  }
  .appointment__line + .appointment__line { margin-top: 36px; }
  .contact-band {
    position: absolute;
    left: 0; right: 0; bottom: 0;
    height: 300px;
  }
  .contact-band svg.band { position: absolute; inset: 0; }
  .contact-list {
    position: absolute;
    left: 28px; right: 20px; top: 92px;
    list-style: none;
  }
  .contact-list li {
    display: flex;
    align-items: center;
    gap: 10px;
    font-size: 13px;
    color: var(--paper-ink);
    margin-bottom: 21px;
  }
  .contact-list .icon { width: 14px; height: 14px; flex: none; }
</style>
</head>
<body>
  <section class="card card--front" aria-label="Card front">
    <svg viewBox="0 0 340 580" width="340" height="580" aria-hidden="true">
      <circle cx="200" cy="300" r="236" fill="none" stroke="var(--ring-light)" stroke-width="6"/>
      <circle cx="200" cy="300" r="226" fill="none" stroke="var(--navy)" stroke-width="14"/>
      <circle cx="200" cy="300" r="218" fill="var(--paper)"/>
    </svg>
    <div class="brand-lockup">
      <span class="brand-dot"></span>
      <span class="brand-name">Mist &amp; Mane</span>
    </div>
  </section>

  <section class="card card--back" aria-label="Card back">
    <div class="back-mark">
      <span class="brand-dot"></span>
      <span class="brand-name">Mist &amp; Mane</span>
    </div>

    <div class="appointment">
      <p class="appointment__label">Appointment</p>
      <div class="appointment__line"></div>
      <div class="appointment__line"></div>
    </div>

    <div class="contact-band">
      <svg class="band" viewBox="0 0 340 300" width="340" height="300" preserveAspectRatio="none" aria-hidden="true">
        <path d="M0 14 C70 -6 130 44 200 28 C260 14 300 22 340 44 L340 300 L0 300 Z" fill="var(--navy)"/>
      </svg>
      <ul class="contact-list">
        <li>
          <svg class="icon" viewBox="0 0 16 16" aria-hidden="true"><path d="M3 2h3l1.5 3.5-2 1.2a8 8 0 0 0 3.8 3.8l1.2-2L14 10v3a1 1 0 0 1-1 1A11 11 0 0 1 2 3a1 1 0 0 1 1-1z" fill="#fff"/></svg>
          07 5000 2184
        </li>
        <li>
          <svg class="icon" viewBox="0 0 16 16" aria-hidden="true"><rect x="1" y="3" width="14" height="10" rx="1" fill="#fff"/><path d="M1.5 3.5 8 9l6.5-5.5" fill="none" stroke="var(--navy)" stroke-width="1.3"/></svg>
          salon@MistAndMane.com.au
        </li>
        <li>
          <svg class="icon" viewBox="0 0 16 16" aria-hidden="true"><g fill="none" stroke="#fff" stroke-width="1.3"><circle cx="8" cy="8" r="6.5"/><ellipse cx="8" cy="8" rx="3" ry="6.5"/><path d="M1.5 8h13"/></g></svg>
          MistAndMane.com.au
        </li>
        <li>
          <svg class="icon" viewBox="0 0 16 16" aria-hidden="true"><circle cx="8" cy="8" r="5" fill="#fff"/></svg>
          MistAndManeSalon
        </li>
        <li>
          <svg class="icon" viewBox="0 0 16 16" aria-hidden="true"><path d="M8 1a5 5 0 0 1 5 5c0 4-5 9-5 9S3 10 3 6a5 5 0 0 1 5-5z" fill="#fff"/><circle cx="8" cy="6" r="1.8" fill="var(--navy)"/></svg>
          3/12 Harbour Lane, Coralvale
        </li>
      </ul>
    </div>
  </section>
</body>
</html>
```